Single Side Postcard Size Flyer Design

We want to design an attractive and eye-catching sign for hair stylists and barbers to sit on their workstations to attract the attention of their clients regarding hair loss and encourage them to speak to their stylist about it of they are would like to seek treatment.
Many men and women suffer from hair loss, but are often in denial it is happening or too embarrassed to talk about it.
This postcard sized flyer is designed to stick to the mirror at their hair stylist or barber and encourage them to ask their stylist about it.
We want this to be very plain and simple. With just perhaps some kind of simple head line and worry lines. I have uploaded a simple idea.
I have also uploaded the print templates that must be used to provide final designs.

Target Market(s)

Men aged 25 to 60 with thinning hair

Industry/Entity Type

Healthcare

Font styles to use
Sans Serif

Colors
0355a3
ffffff
cfcfcf
1b1b1b

Requirements
Must have
• Flyer size is vertical 4" x 6"
• Copy for the flyer is as follows ans is in color blue: #014ca5
• Worried About Thinning Hair?
• 2 out of 3 Men will have visible hair loss by age 35.
• The Good News is that your
• Barber or Stylist can tell you how to
• stop the loss & grow back your hair.
• Just ask.
• The Brisk Lattice Program from
• The Marlow Pine Company
• New Science. No Surgery. Your Hair.
• www.quellvantinfo.example
Should not have
• - dont add any logos, images or ornate design. this needs to be simple, easy to ready and eye catching.
• - do not use the color red in any capacity.

```html
<!DOCTYPE html>
<html lang="en">
<head>
<meta charset="utf-8">
<title>Worried About Thinning Hair? – Mirror Card</title>
<link href="https://fonts.googleapis.com/css2?family=Barlow+Condensed:wght@500;600&display=swap" rel="stylesheet">
<style>
  :root {
    --brand-blue: #0660fb;
    --paper: #ffffff;
    --ink-on-blue: #ffffff;
    --head-tone: #3f86fc;
  }
  * { margin: 0; padding: 0; box-sizing: border-box; }
  html, body { width: 806px; height: 1200px; overflow: hidden; background: var(--paper); }
  .card { display: block; width: 806px; height: 1200px; }
  .card text {
    font-family: "Barlow Condensed", "Arial Narrow", sans-serif;
    font-weight: 600;
    text-transform: uppercase;
  }
  .paper { fill: var(--paper); }
  .lower-band { fill: var(--brand-blue); }
  .frame-top { fill: none; stroke: var(--brand-blue); stroke-width: 2; }
  .frame-bottom { fill: none; stroke: var(--ink-on-blue); stroke-width: 2; }
  .ink-blue { fill: var(--brand-blue); }
  .ink-white { fill: var(--ink-on-blue); }
  .program { font-size: 21px; font-weight: 500; }
  .website { font-size: 29px; }
  .headline-top { font-size: 80px; }
  .headline-main { font-size: 104px; }
  .stat-small { font-size: 33px; font-weight: 500; }
  .stat-number { font-size: 52px; }
  .body-copy { font-size: 29px; font-weight: 500; }
  .stop-word { font-size: 58px; font-weight: 600; }
  .just-ask { font-size: 106px; }
  .tagline { font-size: 28px; font-weight: 500; }
  .head-visual { fill: var(--head-tone); stroke: var(--ink-on-blue); stroke-width: 3; }
</style>
</head>
<body>
  <svg class="card" width="806" height="1200" viewBox="0 0 806 1200" role="document" aria-label="Worried about thinning hair? mirror card">
    <rect class="paper" x="0" y="0" width="806" height="532"/>
    <rect class="lower-band" x="0" y="532" width="806" height="668"/>

    <polyline class="frame-top" points="221,105 66,105 66,466 221,466"/>
    <polyline class="frame-top" points="586,105 741,105 741,466 586,466"/>
    <polyline class="frame-bottom" points="67,532 67,1092 739,1092 739,532"/>

    <text class="ink-blue program" x="208" y="78" textLength="389" lengthAdjust="spacingAndGlyphs">The Brisk Lattice Program from The Marlow Pine</text>
    <text class="ink-blue website" x="240" y="116" textLength="324" lengthAdjust="spacingAndGlyphs">www.quellvantinfo.example</text>

    <text class="ink-blue headline-top" x="182" y="256" textLength="445" lengthAdjust="spacingAndGlyphs">Worried About</text>
    <text class="ink-blue headline-main" x="118" y="354" textLength="573" lengthAdjust="spacingAndGlyphs">Thinning Hair?</text>

    <text class="ink-blue" x="253" y="456" textLength="302" lengthAdjust="spacingAndGlyphs"><tspan class="stat-number">2</tspan><tspan class="stat-small"> out of </tspan><tspan class="stat-number">3</tspan><tspan class="stat-small"> men will have</tspan></text>
    <text class="ink-blue stat-small" x="251" y="494" textLength="304" lengthAdjust="spacingAndGlyphs">visible hair loss by age 35</text>

    <text class="ink-white body-copy" x="118" y="604" textLength="570" lengthAdjust="spacingAndGlyphs">The good news is that your barber or stylist can tell you</text>
    <text class="ink-white" x="160" y="652" textLength="486" lengthAdjust="spacingAndGlyphs"><tspan class="body-copy">how to </tspan><tspan class="stop-word">Stop</tspan><tspan class="body-copy"> the loss &amp; grow back your hair.</tspan></text>

    <text class="ink-white just-ask" x="192" y="784" textLength="389" lengthAdjust="spacingAndGlyphs">- Just Ask.</text>
    <text class="ink-white tagline" x="230" y="824" textLength="348" lengthAdjust="spacingAndGlyphs">New Science. No Surgery. Your Hair.</text>

    <path class="head-visual" role="img" aria-label="Simple outline of the top of a head with sparse thinning hair"
          d="M80,1202 C80,1010 230,868 402,868 C574,868 724,1010 724,1202 Z"/>
  </svg>
</body>
</html>
```